Wine label

The label will be 4" tall by 5" wide. This would be the image for the middle of the label. I would like the enclosed picture of the deer (not the hunter) on a label somehow. Thoughts I have are black outline or Clear label with the antlers coming out of the wine name.. Open to other ideas...... The label enclosed is the size and one of the ideas I am considering. The wording need to stay the same.

```html
<!DOCTYPE html>
<html lang="en">
<head>
<meta charset="utf-8">
<title>Hollow Creek Winery – Vignoles Label</title>
<link rel="stylesheet" href="https://fonts.googleapis.com/css2?family=Cormorant+Garamond:wght@500&family=Kaushan+Script&family=Lato:wght@400&family=Oswald:wght@400;700&family=Roboto+Condensed:wght@400;700&display=swap">
<style>
  :root {
    --page: #efefef;
    --strip: #c4c4c4;
    --panel: #0b0b0b;
    --panel-edge: #171717;
    --ink-white: #f4f4f4;
    --ink-grey: #c9c9c9;
    --gold: #8d743f;
    --gold-dim: #7a6436;
    --warning-ink: #1a1a1a;
  }
  html, body {
    margin: 0;
    padding: 0;
    width: 1200px;
    height: 1200px;
    overflow: hidden;
    background: var(--page);
  }
  .label {
    position: absolute;
    left: 33px;
    top: 141px;
    width: 1134px;
    height: 917px;
    display: flex;
  }
  .warning-strip {
    width: 268px;
    height: 100%;
    background: var(--strip);
    display: flex;
    justify-content: center;
    padding-top: 51px;
    box-sizing: border-box;
  }
  .warning-text {
    writing-mode: vertical-rl;
    font-family: "Roboto Condensed", sans-serif;
    font-size: 20px;
    line-height: 32px;
    color: var(--warning-ink);
    text-transform: uppercase;
    margin: 0;
  }
  .warning-text span { display: block; white-space: nowrap; }
  .warning-text strong { font-weight: 700; }
  .front-panel {
    position: relative;
    width: 866px;
    height: 100%;
    background: radial-gradient(ellipse at 50% 40%, var(--panel-edge), var(--panel) 75%);
    color: var(--ink-white);
    text-align: center;
  }
  .front-panel > * { position: absolute; left: 0; right: 0; margin: 0; white-space: nowrap; }
  .winery-name {
    top: 56px;
    font-family: "Cormorant Garamond", serif;
    font-weight: 500;
    font-size: 52px;
    line-height: 60px;
    letter-spacing: 1px;
  }
  .winery-sub {
    top: 128px;
    font-family: "Cormorant Garamond", serif;
    font-weight: 500;
    font-size: 34px;
    line-height: 38px;
  }
  .winery-sub span { border-bottom: 2px solid var(--gold); padding: 0 4px 2px; }
  .deer-art {
    top: 183px;
    left: 323px;
    right: auto;
    width: 220px;
    height: 258px;
  }
  .wine-name {
    top: 425px;
    font-family: "Oswald", sans-serif;
    font-weight: 700;
    font-size: 74px;
    letter-spacing: 2px;
    line-height: 100px;
  }
  .vintage-row {
    top: 566px;
    left: 259px;
    right: 303px;
    display: flex;
    justify-content: space-between;
    font-family: "Kaushan Script", cursive;
    font-size: 27px;
    line-height: 36px;
  }
  .style-block { top: 598px; left: 252px; right: 279px; color: var(--gold); }
  .rule-row {
    display: flex;
    align-items: center;
    gap: 10px;
    font-family: "Lato", sans-serif;
  }
  .rule-row::before, .rule-row::after {
    content: "";
    flex: 1;
    height: 2px;
    background: var(--gold);
  }
  .style-sweet { font-size: 23px; line-height: 28px; }
  .style-type {
    font-family: "Lato", sans-serif;
    font-size: 54px;
    line-height: 58px;
    white-space: nowrap;
  }
  .style-region { font-size: 16px; line-height: 20px; }
  .producer {
    top: 720px;
    left: 262px;
    right: 299px;
    font-family: "Cormorant Garamond", serif;
    font-size: 19px;
    line-height: 25px;
    color: var(--ink-grey);
    padding-bottom: 8px;
    border-bottom: 2px solid var(--gold);
  }
  .legal {
    top: 801px;
    font-family: "Oswald", sans-serif;
    font-size: 13px;
    line-height: 18px;
    color: var(--gold-dim);
    font-style: italic;
  }
  .volume {
    top: 837px;
    font-family: "Oswald", sans-serif;
    font-size: 13px;
    line-height: 18px;
    color: var(--gold-dim);
    font-style: italic;
  }
</style>
</head>
<body>
  <div class="label">
    <aside class="warning-strip">
      <p class="warning-text">
        <span><strong>Government Warning:</strong> (1) According to the Surgeon General, women should not</span>
        <span>drink alcoholic beverages during pregnancy because of the risk of birth defects.</span>
        <span>(2) Consumption of alcoholic beverages impairs your ability to drive a car or</span>
        <span>operate machinery, and may cause health problems.</span>
      </p>
    </aside>
    <section class="front-panel">
      <h1 class="winery-name">Hollow Creek</h1>
      <p class="winery-sub"><span>Winery</span></p>
      <svg class="deer-art" viewBox="0 0 220 258" role="img" aria-label="Illustration of a stag head with large antlers">
        <defs>
          <radialGradient id="deer-tone" cx="50%" cy="45%" r="60%">
            <stop offset="0%" stop-color="#8c8c8c"/>
            <stop offset="100%" stop-color="#1e1e1e"/>
          </radialGradient>
        </defs>
        <rect width="220" height="258" rx="8" fill="url(#deer-tone)"/>
      </svg>
      <h2 class="wine-name">VIGNOLES</h2>
      <div class="vintage-row"><span>Vintage</span><span>2015</span></div>
      <div class="style-block">
        <div class="rule-row style-sweet">A SWEET</div>
        <div class="style-type">WHITE WINE</div>
        <div class="rule-row style-region">JO DAVIESS COUNTY, ILLINOIS</div>
      </div>
      <p class="producer">Grown, Produced and Bottled by<br>Hollow Creek, LLC, Linden Falls, Illinois</p>
      <p class="legal">Sulfites Althol 10%/Vol.</p>
      <p class="volume">750 ml</p>
    </section>
  </div>
</body>
</html>
```